A4 Single Page Brochure for Private Cloud Offerings

Theme: Futuristic Tech Company

Brightmoor Systems is looking to offer private cloud services for our enterprise customers in Perth-based data-centres that provides our clients with a lower-cost alternative to Nimbra or KLT yielding better performance.

We are looking for a single A4 brochure with a great graphics design theme to promote these services.

We will be providing five tiers:
- Starter
- Growth
- Professional
- Premier
- Elite

Each plan must list on the brochure the Max VMs, CPU cores, Memory and SSD storage allocated. Refer to the uploaded PNG file.

The brochure must list the following selling points:

- Hosted in a local Perth-based TIER3 and TIER4 datacentres
- WA owned hosting - support local
- Low latency - ultra fast local hosting
- Includes Quorra Host Datacentre licensing
- Includes WallHaven Managed Firewalls for Enterprise level threat detection
- Includes all infrastructure maintenance services
- Full self management of VMs through customer portal
- Includes a 1gbps Internet link
- Predictable fixed monthly fee with no dynamic billing
- No additional charges for Storage Transactions, Internet Usage, VM Snapshots, Datacentre Bandwidth Usage and Firewall Traffic Usage.
- Highly available cluster, no single point of failure.
- Pricing is based on 36 months commit
- Yearly rate increases capped to a maximum of Australian CPI
- All plans have 24/7/365 support with dedicated after hours number.
- Managed backup and managed disaster recovery services can be added to plans

Service provided in accordance with our terms and conditions.

We need the ability to EDIT the brochure to adjust pricing after we receive the final project.

Please do not utilise "Pushing the Boundaries of Technology" - our brand is being replaced with "Specialised Consulting". New website is under development but not launched yet.

Target Market(s)

Information Technology Sector

Colors
0054AA
0677BA
7BADD7
CADEEF
E8F1F8

Requirements
Must have
• Theme of Brightmoor is Blue
Should not have
• Extremely stock imagary that just looks "cheap and stock"

```html
<!DOCTYPE html>
<html lang="en">
<head>
<meta charset="utf-8">
<title>Brightmoor Systems – Private Cloud Plans</title>
<link href="https://fonts.googleapis.com/css2?family=Orbitron:wght@500;700;800&family=Montserrat:wght@400;500;600;700;800&display=swap" rel="stylesheet">
<style>
  :root{
    --navy:#1a2470;
    --navy-deep:#141c5c;
    --brand:#0054AA;
    --brand-mid:#0677BA;
    --brand-light:#7BADD7;
    --brand-pale:#CADEEF;
    --brand-mist:#E8F1F8;
    --white:#ffffff;
    --ink:#2b2f4a;
  }
  *{margin:0;padding:0;box-sizing:border-box}
  html,body{width:849px;height:1200px;overflow:hidden;background:var(--white)}
  .brochure{position:relative;width:849px;height:1200px;overflow:hidden;background:var(--white);font-family:"Montserrat",sans-serif;color:var(--ink)}

  .header-art{position:absolute;left:0;top:0}
  .title{position:absolute;left:55px;top:64px;font-family:"Orbitron",sans-serif;font-weight:700;color:var(--white);font-size:48px;line-height:53px;letter-spacing:0}
  .title sup{font-size:24px;vertical-align:top;position:relative;top:0}

  .brand{position:absolute;left:628px;top:98px;width:190px;text-align:center}
  .brand-mark{width:58px;height:58px;margin:0 auto 12px;background:var(--brand)}
  .brand-name{font-family:"Orbitron",sans-serif;font-weight:800;color:var(--brand);font-size:18px;letter-spacing:1px;line-height:22px}

  .plan{position:absolute}
  .plan-name{font-family:"Orbitron",sans-serif;font-weight:800;color:var(--brand);font-size:19px;text-align:center;letter-spacing:.5px;height:42px;line-height:24px}
  .plan-card{background:linear-gradient(100deg,var(--navy) 0%,var(--navy-deep) 35%,var(--brand) 100%);color:var(--white);padding:16px 0 0 50px}
  .spec{font-size:16.5px;line-height:20.5px;font-weight:400}
  .spec b{font-weight:700}
  .price{font-size:28px;line-height:34px;font-weight:800;margin-top:14px;letter-spacing:-.3px}
  .price small{font-size:15px;font-weight:400;letter-spacing:0}
  .tag{display:inline-block;margin:14px 0 0 -8px;background:var(--white);color:var(--brand);font-size:16px;line-height:22px;font-weight:500;padding:7px 14px;letter-spacing:.3px}

  .plan--starter{left:17px;top:253px;width:259px}
  .plan--growth{left:293px;top:253px;width:260px}
  .plan--professional{left:570px;top:253px;width:259px}
  .plan--premier{left:154px;top:487px;width:264px}
  .plan--elite{left:433px;top:487px;width:262px}
  .plan--starter .plan-card,.plan--growth .plan-card,.plan--professional .plan-card{height:169px}
  .plan--premier .plan-card,.plan--elite .plan-card{height:225px;padding-left:54px}

  .features{position:absolute;left:30px;top:791px;width:650px;list-style:none}
  .features li{position:relative;padding-left:21px;font-size:13.3px;line-height:19.6px;color:var(--ink);white-space:nowrap}
  .features li svg{position:absolute;left:0;top:4px}
  .features .group-start{margin-top:7.5px}

  .contact-icons{position:absolute;left:545px;top:800px}
  .contact{position:absolute;left:572px;top:790px;width:277px;height:113px;background:linear-gradient(100deg,var(--navy) 0%,var(--brand) 100%);color:var(--white);font-size:12.6px;line-height:16px;padding:11px 0 0 14px;font-style:normal}
  .contact p{margin-bottom:14px}

  .footer{position:absolute;left:0;top:1144px;width:849px;height:56px;background:linear-gradient(90deg,var(--navy-deep),var(--navy) 60%,var(--brand));color:var(--white);font-size:12.8px;font-weight:500;padding:18px 0 0 38px}
</style>
</head>
<body>
<div class="brochure">

  <svg class="header-art" width="849" height="240" viewBox="0 0 849 240" aria-hidden="true">
    <defs>
      <linearGradient id="headBand" x1="0" y1="0" x2="1" y2="0.3">
        <stop offset="0" stop-color="#1a2470"/>
        <stop offset="0.55" stop-color="#162067"/>
        <stop offset="1" stop-color="#0054AA"/>
      </linearGradient>
      <linearGradient id="headGlow" x1="0" y1="1" x2="1" y2="0">
        <stop offset="0" stop-color="#0677BA" stop-opacity="0"/>
        <stop offset="1" stop-color="#0677BA" stop-opacity="0.9"/>
      </linearGradient>
    </defs>
    <polygon points="0,0 612,0 495,214 0,214" fill="url(#headBand)"/>
    <polygon points="360,214 495,214 612,0 520,0" fill="url(#headGlow)"/>
    <polygon points="418,208 612,82 612,92 432,208" fill="#c9ccd6"/>
  </svg>

  <h1 class="title">PRIVATE CLOUD<br>PLANS<sup>*</sup></h1>

  <div class="brand">
    <div class="brand-mark"></div>
    <div class="brand-name">BRIGHTMOOR<br>SYSTEMS</div>
  </div>

  <section class="plan plan--starter">
    <h2 class="plan-name">STARTER</h2>
    <div class="plan-card">
      <p class="spec"><b>5</b> Max VMs</p>
      <p class="spec"><b>8</b> CPU Cores</p>
      <p class="spec"><b>64 GB</b> Memory</p>
      <p class="spec"><b>3 TB</b> SSD Storage</p>
      <p class="price">$1,028.01<small>/mo</small></p>
    </div>
  </section>

  <section class="plan plan--growth">
    <h2 class="plan-name">GROWTH</h2>
    <div class="plan-card">
      <p class="spec"><b>10</b> Max VMs</p>
      <p class="spec"><b>16</b> CPU Cores</p>
      <p class="spec"><b>128 GB</b> Memory</p>
      <p class="spec"><b>8 TB</b> SSD Storage</p>
      <p class="price">$3,426.64<small>/mo</small></p>
    </div>
  </section>

  <section class="plan plan--professional">
    <h2 class="plan-name">PROFESSIONAL</h2>
    <div class="plan-card">
      <p class="spec"><b>15</b> Max VMs</p>
      <p class="spec"><b>32</b> CPU Cores</p>
      <p class="spec"><b>192 GB</b> Memory</p>
      <p class="spec"><b>15 TB</b> SSD Storage</p>
      <p class="price">$4,626.05<small>/mo</small></p>
    </div>
  </section>

  <section class="plan plan--premier">
    <h2 class="plan-name">PREMIER</h2>
    <div class="plan-card">
      <p class="spec"><b>20</b> Max VMs</p>
      <p class="spec"><b>48</b> CPU Cores</p>
      <p class="spec"><b>256 GB</b> Memory</p>
      <p class="spec"><b>20 TB</b> SSD Storage</p>
      <p class="price">$5,482.72<small>/mo</small></p>
      <span class="tag">BEST SELLER!</span>
    </div>
  </section>

  <section class="plan plan--elite">
    <h2 class="plan-name">ELITE</h2>
    <div class="plan-card">
      <p class="spec"><b>25</b> Max VMs</p>
      <p class="spec"><b>64</b> CPU Cores</p>
      <p class="spec"><b>320 GB</b> Memory</p>
      <p class="spec"><b>30 TB</b> SSD Storage</p>
      <p class="price">$7,196.07<small>/mo</small></p>
      <span class="tag">BEST VALUE!</span>
    </div>
  </section>

  <ul class="features">
    <li><svg width="12" height="11" viewBox="0 0 12 11"><path d="M1 6l3.5 3.5L11 1.5" fill="none" stroke="#0054AA" stroke-width="2.4"/></svg>Hosted in a local Perth-based TIER3 and TIER4 datacentres</li>
    <li><svg width="12" height="11" viewBox="0 0 12 11"><path d="M1 6l3.5 3.5L11 1.5" fill="none" stroke="#0054AA" stroke-width="2.4"/></svg>WA owned hosting - support local</li>
    <li><svg width="12" height="11" viewBox="0 0 12 11"><path d="M1 6l3.5 3.5L11 1.5" fill="none" stroke="#0054AA" stroke-width="2.4"/></svg>Low latency - ultra fast local hosting</li>
    <li><svg width="12" height="11" viewBox="0 0 12 11"><path d="M1 6l3.5 3.5L11 1.5" fill="none" stroke="#0054AA" stroke-width="2.4"/></svg>Quorra Host Datacentre licensing</li>
    <li><svg width="12" height="11" viewBox="0 0 12 11"><path d="M1 6l3.5 3.5L11 1.5" fill="none" stroke="#0054AA" stroke-width="2.4"/></svg>WallHaven Managed Firewalls for Enterprise level threat detection</li>
    <li class="group-start"><svg width="12" height="11" viewBox="0 0 12 11"><path d="M1 6l3.5 3.5L11 1.5" fill="none" stroke="#0054AA" stroke-width="2.4"/></svg>All infrastructure maintenance services</li>
    <li><svg width="12" height="11" viewBox="0 0 12 11"><path d="M1 6l3.5 3.5L11 1.5" fill="none" stroke="#0054AA" stroke-width="2.4"/></svg>Full self management of VMs through customer portal</li>
    <li><svg width="12" height="11" viewBox="0 0 12 11"><path d="M1 6l3.5 3.5L11 1.5" fill="none" stroke="#0054AA" stroke-width="2.4"/></svg>1 Gbps Internet link</li>
    <li><svg width="12" height="11" viewBox="0 0 12 11"><path d="M1 6l3.5 3.5L11 1.5" fill="none" stroke="#0054AA" stroke-width="2.4"/></svg>Predictable fixed monthly fee with no dynamic billing</li>
    <li><svg width="12" height="11" viewBox="0 0 12 11"><path d="M1 6l3.5 3.5L11 1.5" fill="none" stroke="#0054AA" stroke-width="2.4"/></svg>No additional charges for Storage Transactions, Internet Usage, VM Snapshots,<br>Datacentre Bandwidth Usage and Firewall Traffic Usage.</li>
    <li class="group-start"><svg width="12" height="11" viewBox="0 0 12 11"><path d="M1 6l3.5 3.5L11 1.5" fill="none" stroke="#0054AA" stroke-width="2.4"/></svg>Highly available cluster, no single point of failure.</li>
    <li><svg width="12" height="11" viewBox="0 0 12 11"><path d="M1 6l3.5 3.5L11 1.5" fill="none" stroke="#0054AA" stroke-width="2.4"/></svg>Pricing is based on 36 months commit</li>
    <li><svg width="12" height="11" viewBox="0 0 12 11"><path d="M1 6l3.5 3.5L11 1.5" fill="none" stroke="#0054AA" stroke-width="2.4"/></svg>Yearly rate increases capped to a maximum of Australian CPI</li>
    <li><svg width="12" height="11" viewBox="0 0 12 11"><path d="M1 6l3.5 3.5L11 1.5" fill="none" stroke="#0054AA" stroke-width="2.4"/></svg>24/7/365 support with dedicated after hours number for all plans</li>
    <li><svg width="12" height="11" viewBox="0 0 12 11"><path d="M1 6l3.5 3.5L11 1.5" fill="none" stroke="#0054AA" stroke-width="2.4"/></svg>Managed backup and managed disaster recovery services can be added to plans</li>
  </ul>

  <svg class="contact-icons" width="22" height="100" viewBox="0 0 22 100" aria-hidden="true">
    <path d="M11 2a6.5 6.5 0 0 0-6.5 6.5C4.5 13.5 11 21 11 21s6.5-7.5 6.5-12.5A6.5 6.5 0 0 0 11 2zm0 9a2.5 2.5 0 1 1 0-5 2.5 2.5 0 0 1 0 5z" fill="#1a2470"/>
    <path d="M6 41c1.5 3.5 4 6 7.5 7.5l2.3-2.3c.4-.4.9-.5 1.3-.3l2.6 1c.4.2.6.6.6 1v3c0 .6-.5 1.1-1.1 1.1C10.5 51 3 43.5 3 34.2c0-.6.5-1.1 1.1-1.1h3c.4 0 .8.2 1 .6l1 2.6c.2.4.1.9-.3 1.3z" fill="#1a2470"/>
    <rect x="3" y="74" width="16" height="11" fill="none" stroke="#1a2470" stroke-width="2"/>
    <path d="M3 74l8 6 8-6" fill="none" stroke="#1a2470" stroke-width="2"/>
  </svg>
  <address class="contact">
    <p>17/3 Harbourline Drive,<br>Coral Bay, 6170, Australia</p>
    <p>08 9000 4120</p>
    <p>support@brightmoorsystems.example</p>
  </address>

  <footer class="footer">*Service provided in accordance with our terms and conditions.</footer>
</div>
</body>
</html>
```